RW Talbrook LLC Business Card - Civil Engineering & Consulting Firm

We need a Business Card that is elegant, and masculine.  It is our Professional Civil Engineering & Consulting Company located in San Antonio TX (Not s construction or builder firm- no gears & no tool images please). We provide civil engineering services including  commercial site plans, grading and drainage plans, utility plans, hydraulics and hydrology, land planning, utility coordination, and other general civil engineering services related to commercial and residential development.
We have 2 existing Logos. We would like to convey reliability, strength, trustworthiness and attention to detail.  Blues and orange tones as per logo We are OK with the use of a darker blue in the mix.  We have 2 logo versions - Full Company Name Logo to go on the back of card, & Small Icon Logo for the front w/ personal Info.

Target Market(s)
Architects, Real Estate Developers, Other Strctural Engineers, Surveyers, General Contractors
Industry/Entity Type
Professional Civil Engineering
Contact Information for Business Card
Name, Position, Address, Cell & Office #, email, and company website
Font styles to use
Other font styles liked:
- Avian
Requirements
Should not have
- No Tools, No Gears, no Cranes, or Construction Equipment.

```html
<!DOCTYPE html>
<html lang="en">
<head>
<meta charset="utf-8">
<title>RW Talbrook LLC – Business Card</title>
<link href="https://fonts.googleapis.com/css2?family=Josefin+Sans:wght@300;400;600&family=Arimo:wght@400&display=swap" rel="stylesheet">
<style>
  :root {
    --stage: #2b2b2b;
    --card-dark: #1a1a1a;
    --card-light: #ffffff;
    --emboss: #5a5a5a;
    --blue: #5b9fd6;
    --orange: #f0922b;
    --ink: #111111;
    --rule: #9a9a9a;
  }
  * { box-sizing: border-box; margin: 0; padding: 0; }
  html, body {
    width: 1200px; height: 1040px; overflow: hidden;
    background: var(--stage);
  }
  .stage {
    position: relative; width: 1200px; height: 1040px;
    display: flex; flex-direction: column; align-items: center; justify-content: center; gap: 60px;
  }
  .card {
    width: 660px; height: 378px; position: relative;
    box-shadow: 0 14px 30px rgba(0,0,0,.45);
  }
  .card--back {
    background: var(--card-dark);
    border-radius: 80px 0 80px 0;
    display: flex; align-items: center; justify-content: center;
  }
  .back-wordmark {
    font-family: "Josefin Sans", sans-serif; font-weight: 300;
    font-size: 64px; letter-spacing: 6px; color: var(--emboss);
    display: flex; align-items: center; gap: 22px;
  }
  .back-wordmark .mark-square { width: 22px; height: 22px; background: var(--emboss); }

  .card--front {
    background: var(--card-light);
    border-radius: 0 80px 0 80px;
    display: flex; align-items: center;
  }
  .front-brand {
    width: 330px; display: flex; align-items: center; justify-content: center; gap: 12px;
    font-family: "Josefin Sans", sans-serif; font-weight: 400;
    font-size: 36px; letter-spacing: 3px; color: var(--blue);
  }
  .front-brand .mark-square { width: 14px; height: 14px; background: var(--orange); }
  .divider { width: 1px; height: 160px; background: var(--rule); }
  .contact { padding-left: 30px; }
  .contact .person {
    font-family: "Josefin Sans", sans-serif; font-weight: 400; font-size: 25px;
    letter-spacing: 1px; color: var(--blue); text-transform: uppercase; line-height: 1;
  }
  .contact .person .surname { color: var(--orange); font-weight: 600; }
  .contact .role {
    font-family: "Arimo", sans-serif; font-size: 15px; letter-spacing: 1px;
    color: var(--orange); text-transform: uppercase; margin: 4px 0 12px;
  }
  .contact ul { list-style: none; font-family: "Arimo", sans-serif; font-size: 16px; color: var(--ink); }
  .contact li { display: flex; align-items: center; gap: 8px; line-height: 24px; }
  .contact li svg { width: 16px; height: 16px; flex: none; }
  .contact .accent { color: var(--orange); }
  .contact address {
    font-style: normal; font-family: "Arimo", sans-serif; font-size: 16px;
    color: var(--ink); margin-top: 10px; line-height: 22px;
  }
</style>
</head>
<body>
<main class="stage">
  <section class="card card--back">
    <div class="back-wordmark"><span class="mark-square"></span>RW Talbrook LLC</div>
  </section>

  <section class="card card--front">
    <div class="front-brand"><span class="mark-square"></span>RW Talbrook LLC</div>
    <div class="divider"></div>
    <div class="contact">
      <p class="person">Marcus <span class="surname">Hale</span></p>
      <p class="role">Managing Director</p>
      <ul>
        <li>
          <svg viewBox="0 0 16 16" aria-hidden="true"><path d="M3 1.5l3 3-1.6 1.6a9 9 0 0 0 5.5 5.5L11.5 10l3 3-2 2C6.5 14.5 1.5 9.5 1 3.5z" fill="var(--blue)"/></svg>
          210-555 018 342
        </li>
        <li>
          <svg viewBox="0 0 16 16" aria-hidden="true"><rect x="1" y="3" width="14" height="10" fill="var(--blue)"/><path d="M1 3l7 6 7-6" stroke="#fff" stroke-width="1.2" fill="none"/></svg>
          office@talbrookcivil.com
        </li>
        <li>
          <svg viewBox="0 0 16 16" aria-hidden="true"><g fill="none" stroke="var(--blue)" stroke-width="1.2"><circle cx="8" cy="8" r="6.5"/><ellipse cx="8" cy="8" rx="3" ry="6.5"/><path d="M1.5 8h13M2.5 4.5h11M2.5 11.5h11"/></g></svg>
          <span>www.<span class="accent">talbrookcivil</span>.com</span>
        </li>
      </ul>
      <address>880, Brookfield Avenue Suite 4<br>78205, San Antonio TX</address>
    </div>
  </section>
</main>
</body>
</html>
```